Sophrologist needs a cool signage at door entrance

I need signage for dr in sophrology based in Belgium (french speaking). The signed should capture the name the "Mireille Vantoorn" - "Naturopathe-Sophrologue-Reiki" and a catchphrase = (Healthy way of life)
« Fais du bien à ton corps, pour que ton âme ait envie d’y rester »
Requirements
Must have
- Hey,
Thats the instagram account for some inspiration www.instagram.com/mireille_serene_wellbeing
Light colors, green, blue
Healthy way of life
Size is 45cm wide on 30 cm high
The signage will be placed in front off woof pannel

```html
<!DOCTYPE html>
<html lang="fr">
<head>
<meta charset="utf-8">
<title>Mireille Vantoorn – Door Sign</title>
<link href="https://fonts.googleapis.com/css2?family=Kalam:wght@300;400&display=swap" rel="stylesheet">
<style>
  :root {
    --page-bg: #ffffff;
    --leaf-green: #8cc63f;
    --soft-green: #a9d37a;
    --sky-blue: #9fd8ea;
    --blush: #f2c9cf;
    --sea-blue: #5fb3c8;
    --stone-warm: #e0a36a;
    --stone-deep: #8a6a5a;
    --text-white: #ffffff;
    --text-shadow: rgba(60, 80, 90, 0.35);
  }
  html, body {
    margin: 0;
    padding: 0;
    width: 943px;
    height: 1200px;
    overflow: hidden;
    background: var(--page-bg);
  }
  .door-sign {
    position: absolute;
    left: 30px;
    top: 305px;
    width: 883px;
    height: 589px;
    overflow: hidden;
    background: linear-gradient(90deg,
      var(--leaf-green) 0%,
      var(--soft-green) 22%,
      var(--sky-blue) 48%,
      var(--blush) 62%,
      var(--sea-blue) 100%);
    font-family: "Kalam", cursive;
    color: var(--text-white);
  }
  .door-sign__photo {
    position: absolute;
    left: 330px;
    top: 0;
    width: 553px;
    height: 589px;
    background:
      radial-gradient(ellipse 38% 55% at 58% 62%, var(--stone-warm) 0%, rgba(224,163,106,0.7) 45%, rgba(138,106,90,0.55) 70%, rgba(95,179,200,0) 100%),
      linear-gradient(180deg, rgba(242,201,207,0.6) 0%, rgba(95,179,200,0.5) 30%, rgba(138,106,90,0.55) 100%);
    -webkit-mask-image: linear-gradient(90deg, transparent 0%, #000 35%);
    mask-image: linear-gradient(90deg, transparent 0%, #000 35%);
  }
  .door-sign__text {
    position: absolute;
    margin: 0;
    white-space: nowrap;
    line-height: 1;
    text-shadow: 2px 3px 3px var(--text-shadow);
    font-weight: 400;
  }
  .door-sign__first-name { left: 74px; top: 58px; font-size: 58px; }
  .door-sign__last-name  { left: 52px; top: 132px; font-size: 82px; }
  .door-sign__services   { left: 52px; top: 240px; font-size: 24px; font-weight: 300; }
  .door-sign__tagline-healthy { left: 52px; top: 316px; font-size: 92px; }
  .door-sign__tagline-way     { left: 67px; top: 420px; font-size: 44px; }
  .door-sign__tagline-life    { left: 232px; top: 400px; font-size: 108px; }
</style>
</head>
<body>
  <main class="door-sign">
    <div class="door-sign__photo" role="img" aria-label="Photo of balanced stacked stones on a rock by a calm lake at sunset"></div>
    <h1 class="door-sign__text door-sign__first-name">Mireille</h1>
    <p class="door-sign__text door-sign__last-name">Vantoorn</p>
    <p class="door-sign__text door-sign__services">Naturopathe | Sophrologue | Reiki</p>
    <p class="door-sign__text door-sign__tagline-healthy">Healthy</p>
    <p class="door-sign__text door-sign__tagline-way">way of</p>
    <p class="door-sign__text door-sign__tagline-life">Life</p>
  </main>
</body>
</html>
```